Business Card Design

Please use the Logo for colors and styles, and create a business card using the following info:

Matthias Lorbeer
Web Developer

Lorbeer Systems
+41 76 418 57 90
matthias@lorbeer-systems.ch
www.lorbeer-systems.ch

Download the logo at http://lorbeer-systems.ch/tl_files/lorbeer_systems.zip

Thanks for your works!

```html
<!DOCTYPE html>
<html lang="de">
<head>
<meta charset="utf-8">
<title>Lorbeer Systems – Visitenkarte</title>
<link rel="stylesheet" href="https://fonts.googleapis.com/css2?family=Questrial&display=swap">
<style>
  :root {
    --paper: #ecebe8;
    --card-white: #ffffff;
    --card-edge: #d6d6d6;
    --navy: #0b4a75;
    --ink: #1d4f7c;
    --brand-light: #dcdee0;
    --white: #ffffff;
  }
  * { margin: 0; padding: 0; box-sizing: border-box; }
  html, body {
    width: 1200px;
    height: 900px;
    overflow: hidden;
    background: var(--paper);
    font-family: "Questrial", "Century Gothic", sans-serif;
  }
  .stage { position: relative; width: 1200px; height: 900px; }

  .card {
    position: absolute;
    box-shadow: 0 1px 4px rgba(0,0,0,0.12);
  }
  .card--front {
    left: 300px; top: 110px;
    width: 597px; height: 331px;
    background: var(--card-white);
    border: 1px solid var(--card-edge);
    color: var(--ink);
  }
  .brand-name {
    position: absolute;
    left: 28px; top: 56px;
    font-size: 62px;
    font-weight: 400;
    letter-spacing: 0;
    color: var(--navy);
    line-height: 1;
    white-space: nowrap;
  }
  .address {
    position: absolute;
    left: 30px; top: 130px;
    font-size: 20px;
    letter-spacing: 0.4px;
  }
  .person { position: absolute; left: 32px; top: 211px; }
  .person__name {
    font-size: 28px;
    font-weight: 700;
    color: var(--navy);
    line-height: 1.2;
    -webkit-text-stroke: 0.6px var(--navy);
  }
  .person__role { font-size: 20px; margin-top: 3px; letter-spacing: 0.4px; }
  .contact {
    position: absolute;
    left: 298px; top: 209px;
    list-style: none;
    font-size: 20px;
    line-height: 25px;
    letter-spacing: 0.3px;
  }

  .card--back {
    top: 560px;
    width: 460px; height: 256px;
    display: flex; align-items: center; justify-content: center;
  }
  .card--back-dark { left: 90px; background: var(--navy); }
  .card--back-light { left: 650px; background: var(--brand-light); }
  .card--back .brand-name {
    position: static;
    font-size: 46px;
  }
  .card--back-dark .brand-name { color: var(--white); }
  .card--back-light .brand-name { color: var(--navy); }
</style>
</head>
<body>
<main class="stage">
  <section class="card card--front" aria-label="Visitenkarte Vorderseite">
    <div class="brand-name">LORBEERSYSTEMS</div>
    <p class="address">Birkenweg 14, CH-9417 Talmatt</p>
    <div class="person">
      <p class="person__name">Matthias Lorbeer</p>
      <p class="person__role">Web Developer</p>
    </div>
    <ul class="contact">
      <li>+41 76 418 57 90</li>
      <li>matthias@lorbeer-systems.ch</li>
      <li>www.lorbeer-systems.ch</li>
    </ul>
  </section>

  <section class="card card--back card--back-dark" aria-label="Visitenkarte Rückseite dunkel">
    <div class="brand-name">LORBEERSYSTEMS</div>
  </section>

  <section class="card card--back card--back-light" aria-label="Visitenkarte Rückseite hell">
    <div class="brand-name">LORBEERSYSTEMS</div>
  </section>
</main>
</body>
</html>
```